Marlow Crest Group (Real Estate and Investment)

A high end, clean design.
We are a real estate company with sales, asset management and investment divisions. We want to use a black and white scheme which is really high end feel. The back of the card can just be the logo (black background with the white writing) as we will probably emboss this when we print)

Target Market(s)

High level investors, high end houses for sale

Industry/Entity Type

Business

Contact Information for Business Card

Name, position, phone number and email address
Glen Varley, Managing Director, 0437259064 and glen@marlowcrest-example.com.au

Requirements
Must have
• Back of the card to be the black background with the white writing (as per the attached images). Would like the capacity to emboss the writing and logo

```html
<!DOCTYPE html>
<html lang="en">
<head>
<meta charset="utf-8">
<title>Marlow Crest Group — Business Card</title>
<link rel="stylesheet" href="https://fonts.googleapis.com/css2?family=Montserrat:wght@300;400;700&display=swap">
<style>
  :root {
    --ink: #000000;
    --paper: #ffffff;
    --backdrop: #e9e9e7;
    --rule: #1a1a1a;
    --shadow: rgba(0, 0, 0, 0.18);
  }
  * { margin: 0; padding: 0; box-sizing: border-box; }
  html, body {
    width: 1200px;
    height: 1200px;
    overflow: hidden;
    background: var(--backdrop);
    font-family: "Montserrat", sans-serif;
  }
  .canvas {
    width: 1200px;
    height: 1200px;
    display: flex;
    flex-direction: column;
    align-items: center;
    justify-content: center;
    gap: 56px;
  }
  .card {
    position: relative;
    width: 840px;
    height: 510px;
    box-shadow: 0 10px 30px var(--shadow);
    overflow: hidden;
  }

  /* Front */
  .card-front { background: var(--paper); color: var(--ink); }
  .card-front .top-band {
    position: absolute;
    top: 0;
    left: 47%;
    right: 0;
    height: 26px;
    background: var(--ink);
  }
  .card-front .brand {
    position: absolute;
    top: 96px;
    left: 0;
    right: 0;
    display: flex;
    align-items: center;
    justify-content: center;
    gap: 14px;
    font-weight: 400;
    font-size: 20px;
    letter-spacing: 0.14em;
    text-transform: uppercase;
  }
  .card-front .brand-dot {
    width: 18px;
    height: 18px;
    border: 1.5px solid var(--ink);
    border-radius: 50%;
  }
  .card-front .identity {
    position: absolute;
    top: 176px;
    left: 0;
    right: 0;
    text-align: center;
  }
  .card-front .person-name {
    font-weight: 700;
    font-size: 40px;
    letter-spacing: 0.01em;
  }
  .card-front .person-role {
    margin-top: 4px;
    font-weight: 300;
    font-size: 24px;
    letter-spacing: 0.03em;
  }
  .card-front .rule {
    position: absolute;
    height: 1.5px;
    background: var(--rule);
  }
  .card-front .rule-upper { top: 318px; left: 230px; right: 40px; }
  .card-front .rule-lower { top: 424px; left: 90px; right: 130px; }
  .card-front .contacts {
    position: absolute;
    top: 354px;
    left: 150px;
    right: 80px;
    display: flex;
    gap: 36px;
    font-weight: 400;
    font-size: 20px;
    letter-spacing: 0.02em;
  }

  /* Back */
  .card-back {
    background: var(--ink);
    color: var(--paper);
    display: flex;
    align-items: center;
    justify-content: center;
  }
  .card-back .brand {
    font-weight: 400;
    font-size: 40px;
    letter-spacing: 0.08em;
    text-transform: uppercase;
  }
</style>
</head>
<body>
  <main class="canvas">
    <section class="card card-front" aria-label="Card front">
      <div class="top-band"></div>
      <div class="brand"><span class="brand-dot"></span><span>Marlow Crest Group</span></div>
      <div class="identity">
        <h1 class="person-name">Glen Varley</h1>
        <p class="person-role">Managing Director</p>
      </div>
      <div class="rule rule-upper"></div>
      <div class="contacts">
        <span class="contact-phone">P: 0437259064</span>
        <span class="contact-email">E: glen@marlowcrest-example.com.au</span>
      </div>
      <div class="rule rule-lower"></div>
    </section>

    <section class="card card-back" aria-label="Card back">
      <p class="brand">Marlow Crest Group</p>
    </section>
  </main>
</body>
</html>
```